Byte Lantern Website

Design and implement (fully coded and ready to launch) website for a professional services company - please see the documents attached and send us an email if there are any questions
Target Market(s)
Market to potential clients about the services we offer and be able to reach us for any consulting opportunities
Industry/Entity Type
Professional Service
Coding
Coded - Design and coding required
Number of Pages Required
3 page
Requirements
Must have
- Single page website design that is SEO optimized
Blog Post
Contact US page
Cool images/ logos for the service offering - not fill the website with text/content
Must be professional looking website
Coded website should also look great on different screens - mobile, tablets etc
Nice to have
- Choose easy neutral colors that compliment the logo colors. Having said that don't use every color in the logo for the website design.
Should not have
- Too many colors and several various different fonts

```html
<!DOCTYPE html>
<html lang="en">
<head>
<meta charset="utf-8">
<title>Byte Lantern – End to End Data Services</title>
<link href="https://fonts.googleapis.com/css2?family=Oswald:wght@500&family=Poppins:wght@400;500;600&display=swap" rel="stylesheet">
<style>
:root{
  --purple:#9b3c9e;
  --blue:#2f5db3;
  --navy:#1f3f8f;
  --orange:#f26a1b;
  --ink:#1d2230;
  --muted:#6a6f7c;
  --pale:#f3f5fb;
  --line:#d9dde8;
  --white:#fff;
  --grad:linear-gradient(100deg,var(--purple) 0%,#6a4aa8 45%,var(--blue) 100%);
}
*{box-sizing:border-box;margin:0;padding:0}
html,body{width:1200px;height:4885px;overflow:hidden}
body{font-family:'Poppins',sans-serif;color:var(--ink);background:var(--white);position:relative}
.abs{position:absolute}
.btn{position:absolute;background:var(--orange);color:var(--white);font:500 18px 'Poppins',sans-serif;border-radius:26px;height:50px;line-height:50px;padding:0 26px;text-transform:uppercase;white-space:nowrap}
.art{position:absolute;border-radius:12px}
p.body{font-size:13.5px;line-height:27px;color:var(--muted)}

/* hero */
.hero{position:absolute;left:0;top:0;width:1200px;height:677px;background:var(--grad);overflow:hidden}
.logo-disc{position:absolute;left:28px;top:-70px;width:290px;height:225px;border-radius:0 0 150px 150px;background:var(--white);box-shadow:-10px 8px 0 rgba(60,60,160,.5)}
.brand{position:absolute;left:72px;top:60px;font:600 25px 'Poppins',sans-serif;color:var(--ink);display:flex;align-items:center;gap:10px}
.brand i{width:18px;height:18px;border-radius:50%;background:var(--orange);display:inline-block}
.nav{position:absolute;top:42px;left:528px;display:flex;gap:24px;font-size:15px;color:var(--white)}
.nav .on{color:var(--orange);border-bottom:2px solid var(--orange)}
.nav-cta{position:absolute;left:950px;top:26px;height:52px;line-height:52px;padding:0 25px;border-radius:26px;background:var(--orange);color:var(--white);font:500 18px 'Poppins',sans-serif}
.hero h1{position:absolute;left:76px;top:238px;font:500 53px/62px 'Oswald',sans-serif;color:var(--white)}
.hero .lead{position:absolute;left:78px;top:372px;width:420px;font-size:16px;line-height:28px;color:var(--white)}
.dots{position:absolute;left:1154px;top:310px;display:flex;flex-direction:column;gap:11px}
.dots span{width:13px;height:13px;border-radius:50%;background:rgba(255,255,255,.35)}
.dots .on{background:transparent;border:2px solid var(--white)}

/* about */
.about-bg{position:absolute;left:-120px;top:640px;width:420px;height:460px;border-radius:50%;background:#fdf0ea}
.kicker{font-size:13px;color:var(--purple)}
h2{font:500 40px 'Poppins',sans-serif;color:var(--ink)}

/* services */
.cloudband{position:absolute;left:0;width:1200px;background:var(--pale)}
.card{position:absolute;top:1412px;width:165px;height:175px;background:var(--white);border-radius:10px;box-shadow:0 6px 18px rgba(40,50,90,.12);text-align:center;font:500 17px/22px 'Poppins',sans-serif;color:var(--navy)}
.card.active{background:linear-gradient(150deg,var(--purple),var(--navy));color:var(--white)}
.card svg{display:block;margin:28px auto 14px}

/* tech */
.tech{position:absolute;left:0;top:2123px;width:1200px;height:417px;background:var(--grad)}
.tech h2{position:absolute;width:1200px;top:60px;text-align:center;color:var(--white)}
.grid{position:absolute;left:246px;top:145px;width:712px;display:grid;grid-template-columns:repeat(4,1fr);grid-template-rows:115px 110px}
.grid div{display:flex;align-items:center;justify-content:center;font:500 24px 'Poppins',sans-serif;color:rgba(255,255,255,.85);border-right:1px solid rgba(255,255,255,.12);border-bottom:1px solid rgba(255,255,255,.12)}
.grid div:nth-child(4n){border-right:0}
.grid div:nth-child(n+5){border-bottom:0}

/* blog */
.post{position:absolute;top:3384px;width:334px;height:493px;background:var(--white);box-shadow:0 4px 14px rgba(40,50,90,.08);text-align:center}
.post .pic{position:absolute;left:0;top:0;width:334px;height:237px;border-radius:0 0 50% 50%/0 0 30% 30%;border-bottom:5px solid var(--purple)}
.date{position:absolute;left:130px;top:200px;width:74px;height:74px;border-radius:50%;background:var(--orange);border:5px solid var(--white);color:var(--white);font:500 26px/30px 'Poppins',sans-serif;padding-top:6px}
.date small{display:block;font-size:12px;line-height:14px}
.post h3{position:absolute;left:0;top:300px;width:100%;font:600 17px 'Poppins',sans-serif}
.post p{position:absolute;top:342px;left:24px;right:24px;font-size:13.5px;line-height:27px;color:var(--muted)}
.post .more{position:absolute;left:0;top:440px;width:100%;display:block;text-align:center;font-size:13.5px;color:var(--orange);text-decoration:underline}

/* contact */
.field{position:absolute;left:612px;width:446px;height:50px;border:1px solid var(--line);border-radius:6px;font-size:13.5px;color:var(--muted);padding:14px 18px}
.field.focus{border:2px solid var(--navy)}

/* footer */
.footer{position:absolute;left:0;top:4541px;width:1200px;height:344px;background:var(--grad);color:var(--white)}
.footer h4{font:500 15px 'Poppins',sans-serif;text-transform:uppercase;margin-bottom:16px}
.footer ul{list-style:none;font-size:14px;line-height:29px}
.footer li::before{content:"";display:inline-block;width:6px;height:6px;border-radius:50%;background:var(--orange);margin-right:12px;vertical-align:middle}
.fcol{position:absolute;top:34px}
.social{position:absolute;left:120px;top:170px;display:flex;gap:12px}
.social span{width:42px;height:42px;border-radius:50%;background:rgba(255,255,255,.25)}
.info{display:flex;gap:16px;font-size:14px;line-height:25px;margin-bottom:16px}
.info svg{flex:none;margin-top:3px}
.copy{position:absolute;left:0;top:284px;width:1200px;border-top:1px solid rgba(255,255,255,.2);text-align:center;padding-top:24px;font-size:14px}
</style>
</head>
<body>

<header class="hero">
  <div class="logo-disc"></div>
  <div class="brand"><i></i>Byte Lantern</div>
  <nav class="nav"><span class="on">Home</span><span>About Us</span><span>Services</span><span>Blog</span><span>Contact Us</span></nav>
  <span class="nav-cta">GET STARTED</span>
  <h1>Byte Lantern Provides<br>End to End Services</h1>
  <p class="lead">architecture, design and development of Data Platforms, Analytic workloads, Data Engineering, Cloud Engineering</p>
  <span class="btn" style="left:77px;top:478px">Contact Us</span>
  <div class="art" role="img" aria-label="Illustration of a person sitting on a ball in front of stacked dashboard windows and charts" style="left:590px;top:130px;width:530px;height:505px;background:linear-gradient(160deg,rgba(255,255,255,.55),rgba(255,255,255,.18))"></div>
  <div class="dots"><span></span><span></span><span></span><span class="on"></span><span></span></div>
</header>

<section class="about">
  <div class="about-bg"></div>
  <div class="art" role="img" aria-label="Illustration of a person working at a laptop inside a circular outline" style="left:104px;top:777px;width:408px;height:341px;border-radius:50%;background:linear-gradient(140deg,#e7ecf8,#fde3d3)"></div>
  <div class="abs kicker" style="left:572px;top:738px">Welcome To</div>
  <h2 class="abs" style="left:572px;top:762px">IT Byte Lantern</h2>
  <p class="abs body" style="left:572px;top:830px;width:480px">Byte Lantern provides end to end services in architecture, design and development of Data Platforms, Analytic workloads, Data Engineering, Cloud Engineering</p>
  <p class="abs body" style="left:576px;top:928px;width:460px">Byte Lantern is a company which intends to be in front of the client's needs, deeply understanding clients' business and delivering and optimizing solutions from the initial phase of scoping the requirements, up to the final delivery</p>
  <span class="btn" style="left:578px;top:1057px">Learn More</span>
</section>

<section class="services">
  <svg class="abs" style="left:0;top:1170px" width="1200" height="180" viewBox="0 0 1200 180" aria-hidden="true">
    <path fill="#f3f5fb" d="M0 180V110C0 40 100 0 190 40C250 -10 360 0 400 60C470 -10 600 -10 660 60C720 0 850 0 900 60C960 10 1080 10 1130 60C1170 60 1200 90 1200 110V180Z"/>
  </svg>
  <div class="cloudband" style="top:1320px;height:800px"></div>
  <h2 class="abs" style="width:1200px;left:0;top:1312px;text-align:center">Our Services</h2>
  <div class="card active" style="left:330px">
    <svg width="64" height="64" viewBox="0 0 64 64" fill="none" stroke="#fff" stroke-width="2.5"><rect x="8" y="14" width="48" height="32" rx="4"/><rect x="22" y="22" width="20" height="16" rx="2"/><path d="M20 54h24M32 46v8"/></svg>
    Platform<br>Architecture</div>
  <div class="card" style="left:518px">
    <svg width="64" height="64" viewBox="0 0 64 64" fill="none" stroke="#2f5db3" stroke-width="2.5"><ellipse cx="32" cy="14" rx="16" ry="6"/><path d="M16 14v32c0 3 7 6 16 6s16-3 16-6V14M16 30c0 3 7 6 16 6s16-3 16-6"/><circle cx="46" cy="46" r="7" fill="#9b3c9e" stroke="none"/></svg>
    Data<br>Engineering</div>
  <div class="card" style="left:705px">
    <svg width="64" height="64" viewBox="0 0 64 64" fill="none" stroke="#2f5db3" stroke-width="2.5"><rect x="12" y="6" width="30" height="48" rx="3"/><path d="M18 16h18M18 26h18M18 36h10"/><path d="M34 50a7 7 0 0 1 2-13 9 9 0 0 1 17 2 6 6 0 0 1 0 11Z" fill="#9b3c9e" stroke="none"/></svg>
    Cloud<br>Developments</div>

  <h2 class="abs" style="left:78px;top:1660px;line-height:46px">Platform<br>Architecture</h2>
  <p class="abs body" style="left:78px;top:1770px;width:490px">Byte Lantern works very closely with clients, product managers to understand the scope of the requirements, discuss myriad of technologies choices available both on on-premise, cloud-native services, storage formats, data governance, ingestions, migration, CI/CD, system integrations and serving layer making the data available to their customers meeting the SLAs.</p>
  <p class="abs body" style="left:78px;top:1940px;width:490px">We help the clients guide through all these choices and make the right decision to build Data Platforms which offer the High Availability, Scalable Architecture, forward looking, and cost effective solutions.</p>
  <div class="art" role="img" aria-label="Illustration of a person sitting cross-legged with a laptop in front of a large browser window" style="left:692px;top:1697px;width:436px;height:350px;background:linear-gradient(150deg,#e1e7f5,#f9dccb)"></div>
</section>

<section class="tech">
  <h2>Our Technology Expertise</h2>
  <div class="grid">
    <div>Hearthmill</div><div>FlowReel</div><div>Cloudvane</div><div>Taskloom</div>
    <div>Emberset</div><div>Quillstream</div><div>Skyhaven</div><div>Frostgrid</div>
  </div>
</section>

<section class="members">
  <div class="abs" style="left:129px;top:2654px;width:407px;height:398px;border-radius:50%;background:var(--navy)"></div>
  <div class="art" role="img" aria-label="Portrait photograph of the company founder in a shirt and tie" style="left:189px;top:2674px;width:346px;height:346px;border-radius:50%;background:linear-gradient(160deg,#eef2f8,#c9d3e3)"></div>
  <h2 class="abs" style="left:612px;top:2603px">Company Members</h2>
  <div class="abs" style="left:618px;top:2660px;font:500 19px 'Poppins',sans-serif;color:var(--purple)">Devan Rao</div>
  <p class="abs body" style="left:622px;top:2706px;width:450px">Devan manages all the client interactions and engineering team at Byte Lantern. Devan has over 15 years of experience in the technology before he founded Byte Lantern.</p>
  <p class="abs body" style="left:622px;top:2797px;width:450px">He managed development of large scale enterprise wide, high performance, scalable, real-time software solutions in Tele-communications, Gaming, Finance, and Insurance Industries.</p>
  <p class="abs body" style="left:622px;top:2916px;width:450px">He spends time working on open source projects, contributions to Tidewell, Emberset connectors and Emberset JobRunner and other projects. In free time, Devan enjoys travelling to historical places, playing sports – run, bike, tennis, ping-pong and spending time with family</p>
  <span class="btn" style="left:622px;top:3069px">Contact Us</span>
</section>

<section class="blog">
  <svg class="abs" style="left:0;top:3140px" width="1200" height="180" viewBox="0 0 1200 180" aria-hidden="true">
    <path fill="#f3f5fb" d="M0 180V110C0 40 100 0 190 40C250 -10 360 0 400 60C470 -10 600 -10 660 60C720 0 850 0 900 60C960 10 1080 10 1130 60C1170 60 1200 90 1200 110V180Z"/>
  </svg>
  <div class="cloudband" style="top:3290px;height:663px"></div>
  <h2 class="abs" style="width:1200px;left:0;top:3303px;text-align:center">Latest Blog</h2>
  <article class="post" style="left:76px">
    <div class="pic" role="img" aria-label="Photo of a developer in glasses lit by screen code" style="background:linear-gradient(160deg,#4b5b74,#1b2433)"></div>
    <div class="date">11<small>March</small></div>
    <h3>Lorem Ipsum is simply dummy.</h3>
    <p>Lorem Ipsum is simply dummy text of the printing and typesetting industry. Lorem Ipsum has been..</p>
    <a class="more">Learn More »</a>
  </article>
  <article class="post" style="left:432px">
    <div class="pic" role="img" aria-label="Photo of a glowing database cylinder on a dark background" style="background:linear-gradient(160deg,#1c3a52,#060d16)"></div>
    <div class="date">11<small>March</small></div>
    <h3>Lorem Ipsum is simply dummy.</h3>
    <p>Lorem Ipsum is simply dummy text of the printing and typesetting industry. Lorem Ipsum has been..</p>
    <a class="more">Learn More »</a>
  </article>
  <article class="post" style="left:789px">
    <div class="pic" role="img" aria-label="Photo of a digital world map with rising data bars" style="background:linear-gradient(160deg,#2b4fbf,#2a0f4a)"></div>
    <div class="date">11<small>March</small></div>
    <h3>Lorem Ipsum is simply dummy.</h3>
    <p>Lorem Ipsum is simply dummy text of the printing and typesetting industry. Lorem Ipsum has been..</p>
    <a class="more">Learn More »</a>
  </article>
</section>

<section class="contact">
  <div class="art" role="img" aria-label="Illustration of a woman in an orange coat holding an SEO sign" style="left:170px;top:3990px;width:380px;height:513px;background:linear-gradient(170deg,#fde4d5,#e4e9f6)"></div>
  <h2 class="abs" style="left:600px;top:4020px">CONTACT US</h2>
  <div class="abs" style="left:608px;top:4080px;font-size:14px;color:var(--muted)">If any questions please send us an email.</div>
  <div class="field focus" style="top:4129px">Name *</div>
  <div class="field" style="top:4190px">Email *</div>
  <div class="field" style="top:4253px">Phone *</div>
  <div class="field" style="top:4315px;height:93px">Message *</div>
  <span class="btn" style="left:609px;top:4427px;padding:0 36px">Submit</span>
</section>

<footer class="footer">
  <div class="abs" style="left:106px;top:100px;font:600 24px 'Poppins',sans-serif;display:flex;align-items:center;gap:10px"><i style="width:16px;height:16px;border-radius:50%;background:var(--orange);display:inline-block"></i>Byte Lantern</div>
  <div class="social"><span></span><span></span><span></span></div>
  <div class="fcol" style="left:347px"><h4>Sitemap</h4><ul><li>Home</li><li>About Us</li><li>Services</li><li>Blog</li><li>Contact Us</li></ul></div>
  <div class="fcol" style="left:612px"><h4>Services</h4><ul><li>Platform Architecture</li><li>Data Engineering</li><li>Cloud Developments</li></ul></div>
  <div class="fcol" style="left:878px;width:250px"><h4>Contact Info</h4>
    <div class="info"><svg width="16" height="20" viewBox="0 0 16 20"><path d="M8 0a8 8 0 0 0-8 8c0 6 8 12 8 12s8-6 8-12a8 8 0 0 0-8-8Z" fill="#f26a1b"/><circle cx="8" cy="8" r="3" fill="#fff"/></svg><span>BYTE LANTERN<br>101 - lorem ipsum simple text print type industry.</span></div>
    <div class="info"><svg width="16" height="16" viewBox="0 0 16 16"><path d="M3 1l3 3-2 2a10 10 0 0 0 6 6l2-2 3 3-2 2C7 15 1 9 1 3Z" fill="#f26a1b"/></svg><span>123 456 7890</span></div>
    <div class="info"><svg width="18" height="14" viewBox="0 0 18 14"><rect width="18" height="14" rx="2" fill="#f26a1b"/><path d="M1 2l8 6 8-6" stroke="#fff" stroke-width="1.5" fill="none"/></svg><span>info@bytelantern.com</span></div>
  </div>
  <div class="copy">© BYTE LANTERN - 2020 All rights reserved.</div>
</footer>

</body>
</html>
```